Praxis für Psychotherapie benötigt Corporate Design
Vielen Dank für das Design. Hat mich auch in der Gestaltung meiner Räumlichkeiten noch mal beeinflusst. Danke nochmal, gute Arbeit. Alles Gute Timo Berwald
Zielgruppe
Praxis für Psychotherapie, Patienten im Alter zwischen 18 und 75 Jahren
Aufgabenstellung
1. Der Origami Kranich muss vorkommen (kann stilisiert, geometrisch aber auch gezeichnet oder skelettiert sein).
2. Meine Handskizze beschreibt die ungefähre Richtung, bin aber auch für eine andere Anordnung offen.
3. Ich mag klare Linien, kann mich aber auch für das un- perfekte, schöne im Wabi Sabi begeistern. Daher hätte ich gerne Vorschläge in beide Richtungen.
4. Für die Visitenkarte sollte das Logo auf die Vorderseite, Adresse usw. auf die Rückseite.

```html
<!DOCTYPE html>
<html lang="de">
<head>
<meta charset="utf-8">
<title>Visitenkarte – Praxis für Psychotherapie Timo Berwald</title>
<link rel="stylesheet" href="https://fonts.googleapis.com/css2?family=Noto+Sans:wght@300;400;700&display=swap">
<style>
  :root {
    --stage: #9a9a9a;
    --card: #f7f7f6;
    --navy: #0e4466;
    --navy-deep: #0a3350;
    --ink: #6b6b6b;
    --ink-strong: #5a5a5a;
    --rule: #8a8a8a;
  }
  * { box-sizing: border-box; margin: 0; padding: 0; }
  html, body {
    width: 1200px; height: 1200px; overflow: hidden;
    background: var(--stage);
    font-family: "Noto Sans", Arial, sans-serif;
  }
  .sheet {
    width: 1200px; height: 1200px;
    display: flex; flex-direction: column; align-items: center; justify-content: center;
    gap: 60px;
  }
  .card {
    position: relative;
    width: 760px; height: 490px;
    background: var(--card);
    box-shadow: 0 10px 30px rgba(0,0,0,.25);
  }

  /* Rückseite: Kontaktdaten */
  .card--back .contact {
    position: absolute; left: 72px; top: 100px;
    color: var(--ink); font-size: 23px; line-height: 1.32;
  }
  .contact .person-name { font-weight: 700; color: var(--ink-strong); }
  .contact .role { font-weight: 400; margin-bottom: 38px; }
  .contact .practice { font-weight: 700; color: var(--ink-strong); }
  .card--back .mark-small {
    position: absolute; right: 64px; top: 90px;
    width: 80px; height: 80px;
  }

  /* Vorderseite: Logo-Ersatz */
  .card--front .lockup {
    position: absolute; left: 90px; top: 150px;
    display: flex; align-items: center; gap: 34px;
  }
  .lockup .mark { width: 190px; height: 190px; flex: none; }
  .lockup .wordmark { display: flex; flex-direction: column; }
  .wordmark .tagline {
    font-weight: 300; font-size: 34px; color: var(--ink);
    padding-bottom: 6px; border-bottom: 1px solid var(--rule);
  }
  .wordmark .owner {
    font-weight: 700; font-size: 36px; color: var(--navy);
    letter-spacing: 1px; margin-top: 6px;
  }
</style>
</head>
<body>
<main class="sheet">

  <section class="card card--back" aria-label="Rückseite der Visitenkarte">
    <div class="contact">
      <p class="person-name">Timo Berwald</p>
      <p class="role">Geschäftsführer</p>
      <p class="practice">Praxis für Psychotherapie</p>
      <p>Lindenweg 7 | 10245 Berlin</p>
      <p>T +49 (0)30 51 20 84 | F +49 (0)30 51 20 86</p>
      <p>www.praxis-berwald.de | info@praxis-berwald.de</p>
    </div>
    <svg class="mark-small" viewBox="0 0 80 80" aria-hidden="true">
      <circle cx="40" cy="40" r="36" fill="var(--navy)"/>
    </svg>
  </section>

  <section class="card card--front" aria-label="Vorderseite der Visitenkarte">
    <div class="lockup">
      <svg class="mark" viewBox="0 0 190 190" aria-hidden="true">
        <circle cx="95" cy="95" r="88" fill="var(--navy-deep)"/>
      </svg>
      <div class="wordmark">
        <span class="tagline">Praxis für Psychotherapie</span>
        <span class="owner">TIMO BERWALD</span>
      </div>
    </div>
  </section>

</main>
</body>
</html>
```